(new) Integrative Nutrition Health Coaching business needs a WordPress theme/website!

Hi! I am launching my health coaching business (brightoakvale Nutrition Coaching) and am need of a site design that I can plug into WordPress. I've attached my logos, social media squares, and one program form template -- I would like the website to reflect and compliment this branding so far (working tagline of "Health is for every body"... though I am open to suggestions). If helpful, my personal IG is @tirasolb as all photos there are my original work.

The site should include blog, about me, contact me, testimonials, and health history form templates that I can customize if needed. The overall look and feel should me minimalist yet warm and inviting. My offerings will enable the client to consider what truly nourishes their lives in addition to the food on their plate. Thanks in advance!

```html
<!DOCTYPE html>
<html lang="en">
<head>
<meta charset="utf-8">
<title>brightoakvale Nutrition Coaching</title>
<link href="https://fonts.googleapis.com/css2?family=Poppins:wght@300;400;500;600&family=Jost:wght@300;400;500&family=Libre+Baskerville&display=swap" rel="stylesheet">
<style>
:root{
  --blue:#0d5f9a;
  --blue-dark:#0a4a7a;
  --ink:#333;
  --muted:#666;
  --wash:#e7f1f6;
  --footer:#f2f3f4;
  --star:#f08a1c;
  --white:#fff;
}
*{margin:0;padding:0;box-sizing:border-box}
html,body{width:1200px;height:4000px;overflow:hidden;background:var(--white)}
body{font-family:'Poppins',sans-serif;color:var(--ink)}
.page{position:relative;width:1200px;height:4000px;overflow:hidden}
.abs{position:absolute}
.hero-photo{left:0;top:0;width:1200px;height:722px;
  background:
    radial-gradient(ellipse 150px 70px at 360px 660px,rgba(25,25,28,.85),rgba(25,25,28,0) 100%),
    radial-gradient(ellipse 110px 150px at 330px 470px,rgba(60,58,60,.55),rgba(60,58,60,0) 100%),
    radial-gradient(ellipse 70px 110px at 400px 380px,rgba(176,130,106,.55),rgba(176,130,106,0) 100%),
    radial-gradient(ellipse 120px 70px at 1150px 480px,rgba(236,138,40,.9),rgba(236,138,40,0) 100%),
    radial-gradient(ellipse 160px 80px at 980px 520px,rgba(150,96,52,.75),rgba(150,96,52,0) 100%),
    radial-gradient(ellipse 90px 50px at 880px 540px,rgba(60,72,130,.55),rgba(60,72,130,0) 100%),
    radial-gradient(ellipse 60px 60px at 1140px 330px,rgba(120,170,70,.55),rgba(120,170,70,0) 100%),
    radial-gradient(ellipse 260px 300px at 150px 250px,rgba(200,195,190,.6),rgba(200,195,190,0) 100%),
    linear-gradient(100deg,#e4e1dd 0%,#d8d4cf 30%,#f1efec 58%,#ebe7e1 80%,#e3cdb0 100%)}
.wave{left:0;top:0}
.social{display:flex;gap:14px;left:120px;top:32px}
.social span{width:14px;height:14px;border-radius:50%;background:#b9bec3;display:block}
.brand{left:450px;top:8px;width:300px;text-align:center}
.brand-mark{width:78px;height:78px;border-radius:50%;border:3px solid var(--blue);margin:0 auto 6px}
.brand-name{font-family:'Jost',sans-serif;font-size:22px;letter-spacing:7px;color:var(--blue);font-weight:400}
.brand-sub{font-family:'Jost',sans-serif;font-size:10px;letter-spacing:3px;color:var(--blue);font-weight:500}
.call{left:935px;top:24px;display:flex;gap:12px;align-items:center}
.call small{display:block;font-size:13px;color:#555}
.call b{font-size:16px;font-weight:500;color:#333}
.nav-line{left:0;top:88px;width:1200px;height:1px;background:rgba(0,0,0,.08)}
.nav{top:111px;font-family:'Jost',sans-serif;font-size:17px;color:#222;display:flex;gap:36px}
.nav .active{color:var(--blue);text-decoration:underline}
.hero-copy{left:600px;top:275px;width:390px;text-align:center}
.hero-kicker{font-size:26px;font-weight:300;color:#555}
.hero-title{font-family:'Libre Baskerville',serif;font-size:52px;line-height:62px;color:#111;margin-top:14px}
.hero-title em{font-style:normal;color:var(--blue)}
.arrow{width:40px;height:40px;border-radius:50%;display:flex;align-items:center;justify-content:center}
.arrow.solid{background:var(--blue)}
.arrow.ring{border:1.5px solid #b8c6d2}
.dots-v{left:1144px;top:306px;display:flex;flex-direction:column;gap:8px}
.dots-v span{width:11px;height:11px;border-radius:50%;border:1.5px solid #aaa}
.dots-v span.on{background:var(--blue);border-color:var(--blue)}
.intro{top:818px;left:0;width:1200px;text-align:center;font-size:20px;line-height:33px;color:#222}
.feature h3{font-size:20px;font-weight:500;color:var(--blue);margin-bottom:8px}
.feature p{font-size:14px;line-height:23px;color:var(--muted)}
.icon-dot{width:54px;height:54px;border-radius:50%;background:var(--blue);display:flex;align-items:center;justify-content:center}
.photo-meadow{background:
    radial-gradient(ellipse 90px 120px at 55% 35%,rgba(160,110,80,.6),rgba(160,110,80,0)),
    radial-gradient(ellipse 110px 90px at 50% 72%,rgba(210,40,120,.95),rgba(210,40,120,0)),
    linear-gradient(160deg,#3f6b22,#6f9a3f 45%,#8fb050 100%)}
.photo-pier{background:
    radial-gradient(ellipse 50px 130px at 52% 40%,rgba(200,110,60,.7),rgba(200,110,60,0)),
    radial-gradient(ellipse 160px 80px at 40% 90%,rgba(140,110,80,.8),rgba(140,110,80,0)),
    linear-gradient(180deg,#f6f0e6,#e6d7c2 55%,#b59c7c)}
.coach-band{left:0;top:1584px;width:1200px;height:746px}
.section-title{left:0;width:1200px;text-align:center;font-family:'Jost',sans-serif;font-size:34px;font-weight:300;color:#222}
.section-title em{font-style:normal;color:var(--blue)}
.section-sub{left:0;width:1200px;text-align:center;font-size:14px;color:#444}
.card{top:1840px;width:240px;height:366px;background:var(--white);box-shadow:0 4px 16px rgba(0,0,0,.06);text-align:center}
.card .pic{width:200px;height:200px;border-radius:50%;margin:19px auto 0}
.card h4{font-size:18px;font-weight:500;color:var(--blue);margin-top:26px}
.card p{font-size:14px;line-height:23px;color:var(--muted);margin-top:10px;padding:0 24px}
.event-side{top:2570px;height:249px;opacity:.6}
.event-main{left:292px;top:2443px;width:616px;height:404px;background:
    radial-gradient(ellipse 170px 110px at 62% 62%,rgba(226,50,140,.95),rgba(226,50,140,0)),
    radial-gradient(ellipse 120px 80px at 40% 50%,rgba(60,170,110,.8),rgba(60,170,110,0)),
    radial-gradient(ellipse 110px 90px at 22% 40%,rgba(50,120,190,.7),rgba(50,120,190,0)),
    radial-gradient(ellipse 140px 90px at 45% 85%,rgba(190,140,110,.7),rgba(190,140,110,0)),
    radial-gradient(ellipse 120px 70px at 80% 30%,rgba(110,70,50,.55),rgba(110,70,50,0)),
    linear-gradient(180deg,#e9e6e1 0%,#d8d3cb 50%,#b9ad96 100%)}
.event-caption{left:292px;top:2847px;width:616px;height:96px;background:var(--blue);color:#fff;font-size:18px;padding:36px 28px}
.btn{left:519px;top:2990px;width:161px;height:41px;background:var(--blue);color:#fff;font-size:15px;font-weight:500;text-align:center;line-height:41px}
.rule{top:3157px;height:2px;width:60px;background:var(--blue)}
.testi{top:3238px;width:270px}
.stars{color:var(--star);font-size:21px;letter-spacing:2px;line-height:24px}
.testi h5{font-size:15px;font-weight:600;color:#222;margin-top:14px;white-space:nowrap}
.testi p{font-size:13.5px;line-height:24px;color:var(--muted);margin-top:14px;width:255px}
.author{display:flex;gap:16px;align-items:center;margin-top:44px}
.avatar{width:38px;height:38px;border-radius:50%;background:linear-gradient(135deg,#9a9a9a,#444)}
.author b{display:block;font-size:14px;font-weight:500;color:#222}
.author span{font-size:14px;color:#555}
.testi-card{left:435px;top:3207px;width:329px;height:315px;background:#fff;box-shadow:0 4px 24px rgba(0,0,0,.08)}
.dots-h{left:568px;top:3571px;display:flex;gap:7px}
.dots-h span{width:11px;height:11px;border-radius:50%;border:1.5px solid #aaa}
.dots-h span.on{background:#e32020;border-color:#e32020}
.footer-bg{left:0;top:3660px;width:1200px;height:340px;background:var(--footer)}
.foot-h{font-size:15px;font-weight:600;color:#222}
.foot-t{font-size:13px;line-height:22px;color:#333}
.foot-row{display:flex;gap:14px;align-items:flex-start}
.cta{left:840px;top:3841px;width:176px;height:46px;background:var(--blue);color:#fff;font-size:17px;display:flex;align-items:center}
.cta i{width:46px;height:46px;border-radius:50%;background:#0a2c48;display:flex;align-items:center;justify-content:center;margin-left:-4px;margin-right:10px}
.bottom-line{left:0;top:3929px;width:1200px;height:1px;background:#ddd}
.copy{top:3954px;font-size:13px;color:#333}
</style>
</head>
<body>
<main class="page">

  <!-- Hero -->
  <div class="abs hero-photo" role="img" aria-label="Woman in a yoga pose in a bright studio beside a bowl of fruit and granola"></div>
  <svg class="abs wave" width="1200" height="760" viewBox="0 0 1200 760">
    <path d="M0 712 C200 730 420 700 600 660 C820 610 1000 580 1200 585 L1200 760 L0 760 Z" fill="#fff"/>
    <path d="M0 712 C200 730 420 700 600 660 C820 610 1000 580 1200 585" fill="none" stroke="#5b8fb5" stroke-width="3"/>
  </svg>

  <div class="abs social"><span></span><span></span><span></span></div>
  <div class="abs brand">
    <div class="brand-mark"></div>
    <div class="brand-name">BRIGHTOAKVALE</div>
    <div class="brand-sub">NUTRITION COACHING</div>
  </div>
  <div class="abs call">
    <svg width="24" height="24" viewBox="0 0 24 24" fill="none" stroke="#555" stroke-width="1.6"><path d="M5 3h4l2 5-3 2a11 11 0 0 0 6 6l2-3 5 2v4a2 2 0 0 1-2 2A17 17 0 0 1 3 5a2 2 0 0 1 2-2z"/></svg>
    <div><small>Call Us</small><b>555.010.2400</b></div>
  </div>
  <div class="abs nav-line"></div>
  <nav class="abs nav" style="left:121px"><span class="active">Home</span><span>About Me</span><span>Health History</span></nav>
  <nav class="abs nav" style="left:835px"><span>Testimonials</span><span>Blog</span><span>Contact</span></nav>

  <div class="abs hero-copy">
    <div class="hero-kicker">Nutrition Health Coaching</div>
    <div class="hero-title"><em>Health</em> is for<br>every body</div>
  </div>
  <div class="abs arrow ring" style="left:120px;top:319px"><svg width="14" height="14" viewBox="0 0 14 14"><path d="M9 2 4 7l5 5" fill="none" stroke="#8aa2b6" stroke-width="2"/></svg></div>
  <div class="abs arrow solid" style="left:1039px;top:319px"><svg width="14" height="14" viewBox="0 0 14 14"><path d="M5 2l5 5-5 5" fill="none" stroke="#fff" stroke-width="2"/></svg></div>
  <div class="abs dots-v"><span></span><span class="on"></span><span></span><span></span></div>

  <!-- Intro -->
  <p class="abs intro">Lorem Ipsum is simply dummy text<br>of the printing and typesetting industry.</p>

  <!-- Benefits -->
  <svg class="abs" style="left:0;top:930px" width="1200" height="640" viewBox="0 0 1200 640">
    <g fill="none" stroke="#eceff2" stroke-width="1.5">
      <circle cx="600" cy="450" r="460"/>
      <circle cx="600" cy="450" r="350"/>
      <circle cx="600" cy="450" r="240"/>
    </g>
    <path d="M518 68 H640" stroke="var(--blue)" stroke-width="3"/>
    <path d="M458 428 V442 H590" fill="none" stroke="var(--blue)" stroke-width="3"/>
  </svg>
  <div class="abs photo-meadow" style="left:420px;top:1006px;width:270px;height:340px;clip-path:polygon(12% 0,100% 0,88% 100%,0 100%)" role="img" aria-label="Woman in a pink top relaxing in a green meadow"></div>
  <div class="abs photo-pier" style="left:585px;top:978px;width:230px;height:427px;clip-path:polygon(30% 0,100% 0,70% 100%,0 100%)" role="img" aria-label="Woman in a tree yoga pose on a wooden pier"></div>

  <div class="abs feature" style="left:111px;top:1070px;width:200px;text-align:right">
    <h3>Improve Flexibility</h3>
    <p>Lorem Ipsum is simply dummy text of the printing and typesetting industry.</p>
  </div>
  <div class="abs icon-dot" style="left:330px;top:1091px"><svg width="26" height="26" viewBox="0 0 24 24" fill="none" stroke="#fff" stroke-width="1.6"><path d="M12 20s-8-5-8-11a4.5 4.5 0 0 1 8-2.5A4.5 4.5 0 0 1 20 9c0 6-8 11-8 11z"/></svg></div>

  <div class="abs feature" style="left:893px;top:1070px;width:200px">
    <h3>Better Bone Health</h3>
    <p>Lorem Ipsum is simply dummy text of the printing and typesetting industry.</p>
  </div>
  <div class="abs icon-dot" style="left:819px;top:1091px"><svg width="26" height="26" viewBox="0 0 24 24" fill="none" stroke="#fff" stroke-width="1.6"><path d="M12 3v5M12 16v5M3 12h5M16 12h5M6 6l3 3M15 15l3 3"/></svg></div>

  <div class="abs feature" style="left:98px;top:1406px;width:220px;text-align:right">
    <h3>Build Muscle Strength</h3>
    <p>Lorem Ipsum is simply dummy text of the printing and type-setting industry.</p>
  </div>
  <div class="abs icon-dot" style="left:338px;top:1425px"><svg width="26" height="26" viewBox="0 0 24 24" fill="none" stroke="#fff" stroke-width="1.6"><path d="M6 16V11a6 6 0 0 1 12 0v5l2 2H4zM10 21h4"/></svg></div>

  <div class="abs feature" style="left:879px;top:1406px;width:200px">
    <h3>Increase lood Flow</h3>
    <p>Lorem Ipsum is simply dummy text of the printing and typesetting industry.</p>
  </div>
  <div class="abs icon-dot" style="left:807px;top:1425px"><svg width="26" height="26" viewBox="0 0 24 24" fill="none" stroke="#fff" stroke-width="1.6"><path d="M13 3 6 14h6l-1 7 7-11h-6z"/></svg></div>

  <!-- Coaching programmes -->
  <svg class="abs coach-band" width="1200" height="746" viewBox="0 0 1200 746">
    <path d="M0 90 C150 -10 350 20 560 80 C800 150 1000 120 1200 40 L1200 746 L0 746 Z" fill="#e7f1f6"/>
  </svg>
  <h2 class="abs section-title" style="top:1722px"><em>Our</em> Coching</h2>
  <p class="abs section-sub" style="top:1771px">Lorem Ipsum is simply dummy text of the printing</p>

  <div class="abs arrow ring" style="left:154px;top:2002px;width:30px;height:30px"><svg width="12" height="12" viewBox="0 0 14 14"><path d="M9 2 4 7l5 5" fill="none" stroke="#8aa2b6" stroke-width="2"/></svg></div>
  <div class="abs arrow solid" style="left:1027px;top:2002px;width:30px;height:30px"><svg width="12" height="12" viewBox="0 0 14 14"><path d="M5 2l5 5-5 5" fill="none" stroke="#fff" stroke-width="2"/></svg></div>

  <article class="abs card" style="left:224px">
    <div class="pic" role="img" aria-label="Women stretching in a yoga class" style="background:radial-gradient(circle at 55% 50%,rgba(150,150,155,.8),rgba(150,150,155,0) 35%),radial-gradient(circle at 25% 40%,rgba(230,150,180,.7),rgba(230,150,180,0) 30%),radial-gradient(circle at 50% 90%,rgba(60,80,160,.7),rgba(60,80,160,0) 35%),linear-gradient(180deg,#f3f1ef,#dcd6d8)"></div>
    <h4>Our Coching -1</h4>
    <p>Lorem Ipsum is simply dummy text of the printing and typesetting industry.</p>
  </article>
  <article class="abs card" style="left:488px">
    <div class="pic" role="img" aria-label="Fresh vegetables and a measuring tape" style="background:radial-gradient(circle at 40% 35%,rgba(220,50,30,.95),rgba(220,50,30,0) 30%),radial-gradient(circle at 75% 70%,rgba(80,150,50,.95),rgba(80,150,50,0) 35%),radial-gradient(circle at 30% 75%,rgba(60,30,60,.9),rgba(60,30,60,0) 35%),radial-gradient(circle at 60% 55%,rgba(240,200,50,.9),rgba(240,200,50,0) 30%),linear-gradient(180deg,#b8c8d0,#6a7a50)"></div>
    <h4>Our Coching -2</h4>
    <p>Lorem Ipsum is simply dummy text of the printing and typesetting industry.</p>
  </article>
  <article class="abs card" style="left:753px">
    <div class="pic" role="img" aria-label="Woman eating a salad at a kitchen table" style="background:radial-gradient(circle at 40% 55%,rgba(80,120,180,.85),rgba(80,120,180,0) 35%),radial-gradient(circle at 50% 30%,rgba(120,85,60,.6),rgba(120,85,60,0) 25%),radial-gradient(circle at 70% 85%,rgba(130,190,80,.9),rgba(130,190,80,0) 30%),linear-gradient(180deg,#ebe6dc,#d9d1c2)"></div>
    <h4>Our Coching -3</h4>
    <p>Lorem Ipsum is simply dummy text of the printing and typesetting industry.</p>
  </article>

  <!-- Events -->
  <div class="abs event-side" style="left:0;width:109px;background:linear-gradient(180deg,#d8c0a8,#b08c70 55%,#8a8fc0)" role="img" aria-label="Yoga class event"></div>
  <div class="abs event-side" style="left:134px;width:158px;background:linear-gradient(180deg,#9a8e80,#6f6a70 55%,#8a8fc0)" role="img" aria-label="Group stretching event"></div>
  <div class="abs event-side" style="left:908px;width:160px;background:linear-gradient(180deg,#b8c8d8,#7e95b0 55%,#9aa0c8)" role="img" aria-label="Outdoor fitness event"></div>
  <div class="abs event-side" style="left:1092px;width:108px;background:linear-gradient(180deg,#e0a880,#c47a50 55%,#a898c0)" role="img" aria-label="Yoga retreat event"></div>
  <div class="abs event-main" role="img" aria-label="Group of people doing seated forward stretches on mats"></div>
  <div class="abs event-caption">Lorem Ipsum is simply dummy text of the printing</div>
  <div class="abs arrow ring" style="left:211px;top:2877px"><svg width="16" height="12" viewBox="0 0 16 12"><path d="M15 6H2M6 1 1 6l5 5" fill="none" stroke="#b8c6d2" stroke-width="1.5"/></svg></div>
  <div class="abs arrow ring" style="left:949px;top:2877px"><svg width="16" height="12" viewBox="0 0 16 12"><path d="M1 6h13M10 1l5 5-5 5" fill="none" stroke="#b8c6d2" stroke-width="1.5"/></svg></div>
  <div class="abs btn">View All Evints</div>

  <!-- Testimonials -->
  <h2 class="abs section-title" style="top:3100px"><em>Customer</em> Testimonials</h2>
  <div class="abs rule" style="left:362px"></div>
  <div class="abs rule" style="left:780px"></div>
  <p class="abs section-sub" style="top:3147px">Lorem Ipsum is simply dummy text of the printing</p>

  <div class="abs testi-card"></div>
  <div class="abs testi" style="left:121px">
    <div class="stars">★★★★★</div>
    <h5>"SOLID Service! Vety consistent!"</h5>
    <p>the printing and typesetting industry. Lorem Ipsum has been the industry's standard dummy text ever since the 1500s Lorem Ipsum!</p>
    <div class="author"><div class="avatar"></div><div><b>Marin Holt</b><span>Web Development</span></div></div>
  </div>
  <div class="abs testi" style="left:471px">
    <div class="stars">★★★★★</div>
    <h5>"SOLID Service! Vety consistent!"</h5>
    <p>the printing and typesetting industry. Lorem Ipsum has been the industry's standard dummy text ever since the 1500s Lorem Ipsum!</p>
    <div class="author"><div class="avatar"></div><div><b>Marin Holt</b><span>Web Development</span></div></div>
  </div>
  <div class="abs testi" style="left:823px">
    <div class="stars">★★★★★</div>
    <h5>"SOLID Service! Vety consistent!"</h5>
    <p>the printing and typesetting industry. Lorem Ipsum has been the industry's standard dummy text ever since the 1500s Lorem Ipsum!</p>
    <div class="author"><div class="avatar"></div><div><b>Marin Holt</b><span>Web Development</span></div></div>
  </div>
  <div class="abs dots-h"><span></span><span class="on"></span><span></span><span></span></div>

  <!-- Footer -->
  <div class="abs footer-bg"></div>
  <svg class="abs" style="left:0;top:3620px" width="1200" height="70" viewBox="0 0 1200 70">
    <path d="M0 45 C250 0 520 0 700 30 C850 55 1000 50 1200 20 L1200 70 L0 70 Z" fill="#fff"/>
    <path d="M0 45 C250 0 520 0 700 30 C850 55 1000 50 1200 20 L1200 70 L0 70 Z" fill="var(--footer)" transform="translate(0 14)"/>
    <path d="M60 48 C300 0 520 5 700 34 C860 58 1000 52 1100 38" fill="none" stroke="var(--blue)" stroke-width="5" stroke-linecap="round"/>
  </svg>

  <div class="abs" style="left:121px;top:3722px;width:205px;text-align:center">
    <div class="brand-mark" style="width:62px;height:62px"></div>
    <div class="brand-name" style="font-size:17px;letter-spacing:5px">BRIGHTOAKVALE</div>
    <div class="brand-sub" style="font-size:8px">NUTRITION COACHING</div>
  </div>
  <div class="abs social" style="left:168px;top:3855px;gap:20px"><span style="background:var(--blue)"></span><span style="background:var(--blue)"></span><span style="background:var(--blue)"></span></div>

  <div class="abs" style="left:374px;top:3730px">
    <div class="foot-h">Contact Us</div>
    <div class="foot-row" style="margin-top:18px"><svg width="14" height="18" viewBox="0 0 14 18" fill="none" stroke="#333" stroke-width="1.3"><path d="M7 17s6-6 6-10A6 6 0 0 0 1 7c0 4 6 10 6 10z"/><circle cx="7" cy="7" r="2"/></svg><div class="foot-t">42 Linden Row #4B<br>Austin 78701 TX</div></div>
    <div class="foot-row" style="margin-top:12px"><svg width="16" height="16" viewBox="0 0 24 24" fill="#333"><path d="M5 3h4l2 5-3 2a11 11 0 0 0 6 6l2-3 5 2v4a2 2 0 0 1-2 2A17 17 0 0 1 3 5a2 2 0 0 1 2-2z"/></svg><div class="foot-t">555.010.2400</div></div>
    <div class="foot-row" style="margin-top:14px"><svg width="16" height="12" viewBox="0 0 16 12" fill="#333"><path d="M0 0h16v12H0z"/><path d="M0 0l8 7 8-7" fill="none" stroke="#fff" stroke-width="1.3"/></svg><div class="foot-t">info@brightoakvale.com</div></div>
  </div>

  <div class="abs" style="left:643px;top:3731px">
    <div class="foot-h">Company</div>
    <div class="foot-t" style="margin-top:14px;font-size:12px;line-height:22.5px">Home<br>Vineyard<br>Wines<br>Press<br>Contact Us</div>
  </div>

  <div class="abs" style="left:840px;top:3733px">
    <div class="foot-h">Stil have questions?</div>
    <div class="foot-t" style="margin-top:14px">A representative will aswer your<br>questions as soon as possible.</div>
  </div>
  <div class="abs cta"><i><svg width="20" height="20" viewBox="0 0 24 24" fill="none" stroke="#fff" stroke-width="1.6"><path d="M5 3h4l2 5-3 2a11 11 0 0 0 6 6l2-3 5 2v4a2 2 0 0 1-2 2A17 17 0 0 1 3 5a2 2 0 0 1 2-2z"/></svg></i>Contact Now</div>

  <div class="abs bottom-line"></div>
  <p class="abs copy" style="left:121px">Copyright 2020 brightoakvale. All Rights Reserved.</p>
  <p class="abs copy" style="left:874px;font-size:12px">Privacy Policy &nbsp;|&nbsp; Terms Of Services</p>

</main>
</body>
</html>
```